Business Cards, Letterhead, Corporate Materials

Marlowe Building Group, Inc. needs brand identity and marketing materials.

Target Market(s)

Home Owners, Architects, Engineers.

Contact Information for Business Card

Business Cards for myself the President

Font styles to use
Serif

Colors
3377b5
0255a3
cfdfed
cee9f5
86cae7
0393ce
000000
ffffff
f5f5f5

Requirements
Must have
• My name, my address, my email, phone number, company logo, my title. my contractor's license number, web address.
Nice to have
• Very clean professional modern business cards for company president.

```html
<!DOCTYPE html>
<html lang="en">
<head>
<meta charset="utf-8">
<title>Marlowe Building Group, Inc. — Business Card</title>
<link rel="stylesheet" href="https://fonts.googleapis.com/css2?family=Arimo:wght@400;700&display=swap">
<style>
  :root {
    --navy: #2c3a93;
    --sky: #13a6de;
    --mark-blue: #2a4fa8;
    --ink: #111111;
    --muted: #7a7a7a;
    --rule: #4a4a4a;
    --card-edge: #b5b5b5;
    --white: #ffffff;
    --page: #ffffff;
  }
  * { box-sizing: border-box; margin: 0; padding: 0; }
  html, body { width: 855px; height: 1200px; overflow: hidden; background: var(--page); }
  body { position: relative; font-family: "Arimo", Arial, sans-serif; }

  .card { position: absolute; left: 0; width: 855px; height: 485px; border-radius: 40px; overflow: hidden; }

  .card-front {
    top: 185px;
    background: linear-gradient(180deg, var(--navy) 0%, #245aae 45%, var(--sky) 100%);
  }
  .front-brand { position: absolute; left: 137px; top: 345px; display: flex; align-items: center; gap: 26px; }
  .brand-square { width: 120px; height: 120px; background: var(--white); }
  .brand-name { color: var(--white); font-weight: 400; line-height: 1; }
  .brand-name .line-main { display: block; font-size: 74px; letter-spacing: 2px; }
  .brand-name .line-sub { display: block; font-size: 27px; margin-top: 6px; letter-spacing: 0.5px; }

  .card-back { top: 712px; background: var(--white); border: 2px solid var(--card-edge); }
  .back-brand { position: absolute; left: 112px; top: 140px; width: 200px; display: flex; flex-direction: column; align-items: center; gap: 18px; }
  .back-square { width: 150px; height: 150px; background: linear-gradient(180deg, var(--navy), var(--mark-blue)); }
  .back-name { color: var(--mark-blue); font-size: 30px; font-weight: 700; letter-spacing: 1px; }

  .divider { position: absolute; left: 379px; top: 78px; width: 2px; height: 335px; background: var(--rule); }

  .contact { position: absolute; left: 442px; top: 98px; color: var(--ink); }
  .person-name { font-size: 34px; font-weight: 700; line-height: 1.1; }
  .person-title { font-size: 27px; color: var(--muted); margin-top: 2px; }
  .contact-list { list-style: none; margin-top: 30px; }
  .contact-list li { display: flex; align-items: center; gap: 18px; font-size: 26px; height: 38px; }
  .contact-list svg { width: 26px; height: 26px; fill: #3a3a3a; flex: none; }
  .licence { font-size: 26px; margin-top: 16px; }
</style>
</head>
<body>
  <section class="card card-front">
    <div class="front-brand">
      <div class="brand-square"></div>
      <div class="brand-name">
        <span class="line-main">MARLOWE</span>
        <span class="line-sub">BUILDING GROUP, INC.</span>
      </div>
    </div>
  </section>

  <section class="card card-back">
    <div class="back-brand">
      <div class="back-square"></div>
      <div class="back-name">MARLOWE</div>
    </div>
    <div class="divider"></div>
    <div class="contact">
      <div class="person-name">Person name</div>
      <div class="person-title">President</div>
      <ul class="contact-list">
        <li>
          <svg viewBox="0 0 24 24" aria-hidden="true"><path d="M3 9c0-3 4-5 9-5s9 2 9 5v2h-5V9c-1-1-7-1-8 0v2H3z"/><path d="M6 13h12l2 7H4z"/></svg>
          (0123) 555-0146
        </li>
        <li>
          <svg viewBox="0 0 24 24" aria-hidden="true"><path d="M7 1h10a1 1 0 0 1 1 1v20a1 1 0 0 1-1 1H7a1 1 0 0 1-1-1V2a1 1 0 0 1 1-1zm1 3v14h8V4zm4 15.5a1.2 1.2 0 1 0 0 2.4 1.2 1.2 0 0 0 0-2.4z"/></svg>
          (0123) 555-0146
        </li>
        <li>
          <svg viewBox="0 0 24 24" aria-hidden="true"><path d="M2 5h20v14H2zm2 2v.5l8 5 8-5V7zm0 3v7h16v-7l-8 5z"/></svg>
          person@marlowebuilding.com
        </li>
        <li>
          <svg viewBox="0 0 24 24" aria-hidden="true"><path d="M12 2a10 10 0 1 0 0 20 10 10 0 0 0 0-20zm6.9 9h-3a15 15 0 0 0-1.3-6A8 8 0 0 1 18.9 11zM12 4.1c.9 1.3 1.7 3.9 1.9 6.9h-3.8c.2-3 1-5.6 1.9-6.9zM9.4 5a15 15 0 0 0-1.3 6h-3A8 8 0 0 1 9.4 5zM5.1 13h3a15 15 0 0 0 1.3 6A8 8 0 0 1 5.1 13zM12 19.9c-.9-1.3-1.7-3.9-1.9-6.9h3.8c-.2 3-1 5.6-1.9 6.9zm2.6-.9a15 15 0 0 0 1.3-6h3a8 8 0 0 1-4.3 6z"/></svg>
          www.marlowebuilding.com
        </li>
      </ul>
      <div class="licence">Licence #: 10000000</div>
    </div>
  </section>
</body>
</html>
```